Dishwashing salt packaging label

We need a packaging label design for dishwasher salt. The product prevents lime, calcium and other mineral buildups in dishwashers as well as softening the water for the best washing results possible.

The brand name is Morvada.

As part of the design a logo and colour scheme/theme are required.
Updates

Target Market(s)

25-55 year olds

Industry/Entity Type

Product

Requirements
Must have
• The packaging is in the form of a pail. The design should be in the form of labels that are stuck on to the area below the flange. The design should also be provided in a format that allows a printer to manipulate the images for printing.

The pail dimensions are shown in the attached pail_specification.pdf file. The pail size is the 2 litre size. An image of the pail is shown in the attached Pail_Image.jpeg file.

Not shown in the pdf document are the following dimensions:

Height from base to flange: 126mm
Diameter directly below the flange: 150mm

The label should have the following information on it:

Australian Owned and Manufactured
www.morvada.com.au
57 Hollow St, Carden Ridge, Queensland, Australia

I would also like to be provided with images of the logo design and elements of the label design separately.

Nice to have
• If you consider that any slogan or other wording is necessary or desirable on the packaging, suggestions are welcome.

The design should look modern and clean.

```html
<!DOCTYPE html>
<html lang="en">
<head>
<meta charset="utf-8">
<title>Morvada Dishwasher Salt – Pail Label</title>
<link rel="stylesheet" href="https://fonts.googleapis.com/css2?family=Orbitron:wght@500;600&family=Open+Sans:ital,wght@1,600;1,700&display=swap">
<style>
  :root {
    --backdrop: #161616;
    --label-white: #f4f4f2;
    --lime: #b9bd1f;
    --lime-deep: #a9ad14;
  }
  * { margin: 0; padding: 0; box-sizing: border-box; }
  html, body {
    width: 1200px; height: 900px; overflow: hidden;
    background: var(--backdrop);
  }
  .canvas {
    position: relative; width: 1200px; height: 900px;
  }
  .label {
    position: absolute; left: 280px; top: 140px;
    width: 640px; height: 660px;
    background: var(--label-white);
    overflow: hidden;
  }
  .label__bands {
    position: absolute; inset: 0; width: 100%; height: 100%;
  }
  .label__bands path { fill: var(--lime); }
  .label__content {
    position: absolute; inset: 0;
    display: flex; flex-direction: column; align-items: center;
    color: var(--lime-deep);
    text-align: center;
  }
  .brand {
    margin-top: 130px;
    display: flex; align-items: center; gap: 16px;
  }
  .brand__mark {
    width: 22px; height: 22px; background: var(--lime-deep);
  }
  .brand__name {
    font-family: "Orbitron", sans-serif;
    font-weight: 600; font-size: 74px; letter-spacing: 2px;
    text-transform: uppercase; line-height: 1;
  }
  .variant {
    margin-top: 44px; align-self: flex-end; margin-right: 70px;
    font-family: "Orbitron", sans-serif;
    font-weight: 500; font-size: 28px; letter-spacing: 1.5px;
  }
  .product-name {
    margin-top: 66px;
    font-family: "Orbitron", sans-serif;
    font-weight: 600; font-size: 38px; letter-spacing: 2px;
  }
  .benefit {
    margin-top: 22px; width: 360px;
    font-family: "Open Sans", sans-serif;
    font-style: italic; font-weight: 600; font-size: 16px; line-height: 1.35;
  }
  .net-weight {
    margin-top: 36px;
    font-family: "Open Sans", sans-serif;
    font-style: italic; font-weight: 700; font-size: 30px; letter-spacing: 0.5px;
  }
  .maker-details {
    margin-top: 26px;
    font-family: "Open Sans", sans-serif;
    font-style: italic; font-weight: 600; font-size: 11.5px; line-height: 1.4;
    list-style: none;
  }
</style>
</head>
<body>
<main class="canvas">
  <section class="label" aria-label="Morvada dishwasher salt pail label">
    <svg class="label__bands" viewBox="0 0 640 660" preserveAspectRatio="none" aria-hidden="true">
      <path d="M0 0 H255 C120 90 30 260 18 660 H0 Z"/>
      <path d="M640 0 V660 H560 C625 470 630 230 525 0 Z"/>
    </svg>
    <div class="label__content">
      <div class="brand">
        <span class="brand__mark"></span>
        <span class="brand__name">Morvada</span>
      </div>
      <p class="variant">LEMON FRESH</p>
      <h1 class="product-name">DISHWASHER SALT</h1>
      <p class="benefit">Prevents lime, calcium and other mineral buildups in dishwashers and softens water for amazing results.</p>
      <p class="net-weight">2 KG NETT</p>
      <ul class="maker-details">
        <li>Australian Owned and Manufactured</li>
        <li>www.morvada.com.au</li>
        <li>57 Hollow St, Carden Ridge, Queensland, Australia</li>
      </ul>
    </div>
  </section>
</main>
</body>
</html>
```